TORV Brand Template for Customers in Oil & Gas industry

We need our PPTs to look more professional, cleaner, and provide a highlight to our value propositions.

We have hundreds of professional marketing photos, a brand guide, logo files, and a website where you can draw inspiration from. Please leave spaces for our photos. I will choose which to feature on which page.

Please follow our brand guide/colors.

We are a market leader in Oil & Gas and our presentations need to reflect that. Our customers are engineers, so no fluff, just facts/data/science.

Attached is our fonts (Anton=headings, Nueu= body text). Also attached is a template I made. Please use it as a base.

We want a template that looks like we are Castrelle, or Pale Orbit. We sell a premium product that is engineered to be a solution for very difficult problems in the oilfield. We sell it using facts and data, not schtick or fluff.

Each slide should say TORV and have plenty of room for photos and information. Our customers come from major companies and they do not have time for poorly-crafted pitch decks.

Target Market(s)

Production Engineers in Oil & Gas

Industry/Entity Type

Oil & Gas

Font styles to use
Other font styles liked:
• Anton, Neue Haas Groteske

Colors

Requirements
Must have
• Branding, clarity
Nice to have
• If you can use the attached template as a starting point, that would be great.
Should not have
• Anything outside our branding

```html
<!DOCTYPE html>
<html lang="en">
<head>
<meta charset="utf-8">
<title>TORV Presentation Template</title>
<link href="https://fonts.googleapis.com/css2?family=Montserrat:wght@400;500;600;700;800&family=Roboto+Condensed:wght@400;500;700&display=swap" rel="stylesheet">
<style>
:root{
  --red:#b5281f;
  --slate:#4b5669;
  --ink:#3a4150;
  --muted:#6b7080;
  --paper:#ffffff;
  --canvas:#e4e5e8;
  --line:#d6d8dc;
}
*{margin:0;padding:0;box-sizing:border-box}
html,body{width:906px;height:1200px;overflow:hidden}
body{background:var(--canvas);position:relative;font-family:"Montserrat",sans-serif;color:var(--ink)}
.slide{position:absolute;width:500px;height:281px;background:var(--paper);overflow:hidden;transform:scale(.5422);transform-origin:0 0;box-shadow:0 2px 6px rgba(0,0,0,.18)}
.c1{left:36px}.c2{left:318px}.c3{left:599px}
.r1{top:34px}.r2{top:197px}.r3{top:361px}.r4{top:524px}.r5{top:688px}.r6{top:851px}.r7{top:1015px}
.abs{position:absolute}
.title{position:absolute;font-family:"Roboto Condensed",sans-serif;font-weight:500;font-size:19px;color:var(--slate);line-height:1.2}
.title::after{content:"";display:block;width:32px;height:3px;background:var(--red);margin-top:6px}
.title.big{font-size:19px;line-height:1.35}
.logo{position:absolute;top:12px;right:14px;font-family:"Montserrat",sans-serif;font-weight:800;font-size:12px;color:var(--ink);letter-spacing:.5px;display:flex;align-items:center;gap:4px}
.logo::before{content:"";width:7px;height:7px;background:var(--red)}
.foot{position:absolute;left:13px;bottom:9px;font-size:6px;letter-spacing:2px;color:var(--red)}
.pg{position:absolute;right:14px;bottom:9px;font-size:5px;color:var(--ink)}
.ph{position:absolute}
.ph.sky{background:linear-gradient(180deg,#8fb2d6 0%,#c8d7e6 50%,#7b6a55 100%)}
.ph.dusk{background:linear-gradient(160deg,#f2b45b 0%,#b8683a 45%,#3a3a3e 100%)}
.ph.sea{background:linear-gradient(180deg,#d9b7c4 0%,#9fb6d4 50%,#234a78 100%)}
.ph.field{background:linear-gradient(180deg,#c9d4df 0%,#8a9a7a 55%,#6b5a44 100%)}
.ph.plant{background:linear-gradient(180deg,#9aa9c4 0%,#6d7c95 55%,#3f4656 100%)}
.ph.smoke{background:linear-gradient(180deg,#6d93c4 0%,#e6ebf0 45%,#a56a4b 100%)}
.ph.sunset{background:linear-gradient(180deg,#4a6a9a 0%,#e3a06a 55%,#3c3f48 100%)}
.tx{font-size:5.5px;line-height:1.4;color:var(--muted)}
.tx.j{text-align:justify}
.h6{font-size:8px;font-weight:600;color:var(--ink)}
.h6.red{color:var(--red)}
.icon{position:absolute;width:30px;height:30px;display:flex;align-items:center;justify-content:center}
.icon.red{background:var(--red)}.icon.slate{background:var(--slate)}
.num{display:inline-flex;align-items:center;justify-content:center;background:var(--slate);color:#fff;font-weight:700}
.num.red{background:var(--red)}
.part{position:absolute;inset:0;background:linear-gradient(180deg,#5a6478 0%,#4b5669 100%)}
.partbox{position:absolute;left:102px;top:95px;width:295px;height:92px;border:1px solid rgba(255,255,255,.8)}
.partflag{position:absolute;left:102px;top:95px;width:94px;height:92px;background:var(--red);clip-path:polygon(0 0,100% 0,55% 100%,0 100%)}
.partnum{position:absolute;left:112px;top:96px;font-size:72px;font-weight:800;color:#fff;letter-spacing:-4px;line-height:1.25}
.parttitle{position:absolute;left:212px;top:110px;font-size:15px;color:#fff;font-weight:500}
.partsub{position:absolute;left:212px;top:133px;width:170px;font-size:5.5px;line-height:1.4;color:#fff}
.dot{display:inline-block;width:5px;height:5px;border-radius:50%;background:var(--red);margin-right:3px}
</style>
</head>
<body>

<!-- 1 cover -->
<section class="slide c1 r1">
  <div class="abs" style="left:11px;top:11px;width:17px;height:17px;background:var(--red)"></div>
  <div class="abs" style="left:38px;top:60px;font-weight:800;font-size:34px;color:var(--ink);letter-spacing:1px">TORV</div>
  <div class="abs" style="left:24px;top:147px;font-size:22px;color:var(--slate);line-height:1">Business</div>
  <div class="abs" style="left:24px;top:168px;font-size:24px;font-weight:700;color:var(--red);line-height:1">Marketing</div>
  <div class="abs" style="left:24px;top:200px;font-size:9px;color:var(--muted);line-height:1.2">Oil and Gas<br>Consulting Company</div>
  <div class="abs" style="left:35px;top:250px"><span class="dot" style="background:var(--slate)"></span><span class="dot"></span><span class="dot" style="background:var(--slate)"></span></div>
  <div class="ph dusk" role="img" aria-label="Photo: engineers in hard hats at a refinery at sunset" style="left:210px;top:0;width:290px;height:228px"></div>
  <div class="abs" style="left:210px;top:228px;width:290px;height:53px;background:var(--slate);color:#fff;font-size:9px;letter-spacing:3px;text-align:center;line-height:53px">TORVUSA.COM</div>
</section>

<!-- 2 cover alt -->
<section class="slide c2 r1">
  <div class="abs" style="left:315px;top:0;width:185px;height:148px;background:var(--slate)"></div>
  <div class="abs" style="left:197px;top:248px;width:303px;height:33px;background:var(--red)"></div>
  <div class="abs" style="left:246px;top:24px;width:232px;height:238px;background:#fff"></div>
  <div class="ph sea" role="img" aria-label="Photo: offshore oil platform at dusk" style="left:252px;top:30px;width:220px;height:226px"></div>
  <div class="abs" style="left:450px;top:35px;width:15px;height:15px;background:var(--red)"></div>
  <div class="abs" style="left:46px;top:45px;font-weight:800;font-size:34px;color:var(--ink);letter-spacing:1px">TORV</div>
  <div class="abs" style="left:38px;top:138px;font-size:22px;color:var(--slate);line-height:1">Business</div>
  <div class="abs" style="left:38px;top:159px;font-size:24px;font-weight:700;color:var(--red);line-height:1">Marketing</div>
  <div class="abs" style="left:38px;top:192px;font-size:9px;color:var(--muted);line-height:1.2">Oil and Gas<br>Consulting Company</div>
  <div class="abs" style="left:38px;top:252px;font-size:8px;letter-spacing:3px;color:var(--ink)">torvusa.com</div>
</section>

<!-- 3 agenda -->
<section class="slide c3 r1">
  <div class="title" style="left:17px;top:10px">Agenda</div>
  <div class="logo">TORV</div>
  <div class="ph field" role="img" aria-label="Photo: pumpjack in a field" style="left:58px;top:58px;width:155px;height:182px"></div>
  <div class="abs" style="left:232px;top:66px;width:200px">
    <div style="margin-bottom:11px"><div class="h6"><span style="color:var(--red)">1.</span> Lorem ipsum</div><div class="tx">Lorem ipsum dolor sit amet, consectetuer adipiscing elit, sed diam nonummy nibh euismod tincid</div></div>
    <div style="margin-bottom:11px"><div class="h6"><span style="color:var(--red)">2.</span> Lorem ipsum</div><div class="tx">Lorem ipsum dolor sit amet, consectetuer adipiscing elit, sed diam nonummy nibh euismod tincid</div></div>
    <div style="margin-bottom:11px"><div class="h6"><span style="color:var(--red)">3.</span> Lorem ipsum</div><div class="tx">Lorem ipsum dolor sit amet, consectetuer adipiscing elit, sed diam nonummy nibh euismod tincid</div></div>
    <div><div class="h6"><span style="color:var(--red)">4.</span> Lorem ipsum</div><div class="tx">Lorem ipsum dolor sit amet, consectetuer adipiscing elit, sed diam nonummy nibh euismod tincid</div></div>
  </div>
  <div class="foot">torvusa.com</div><div class="pg">2</div>
</section>

<!-- 4 intro -->
<section class="slide c1 r2">
  <div class="title big" style="left:30px;top:22px">Lorem Ipsum<br>Dolor Sit<br>Ametkeeper.</div>
  <div class="logo">TORV</div>
  <div class="ph plant" role="img" aria-label="Photo: processing plant with steam" style="left:178px;top:52px;width:322px;height:123px"></div>
  <div class="abs tx" style="left:30px;top:115px;width:130px">Lorem ipsum dolor sit amet, consectetuer adipiscing elit, sed diam nonummy nibh euismod tincidunt ut laoreet dolore magna aliquam erat volutpat.<br><br>Ut wisi enim ad minim veniam, quis nostrud exerci tation ullamcorper suscipit lobortis nisl ut aliquip ex ea commodo consequat. Duis autem vel eum iriure dolor in hendrerit in vulputate velit esse molestie consequat.<br><br>Vel illum dolore eu feugiat nulla facilisis at vero eros et accumsan et iusto odio dignissim qui blandit praesent luptatum.</div>
  <div class="abs tx" style="left:178px;top:185px;width:300px">Lorem ipsum dolor sit amet, consectetuer adipiscing elit, sed diam nonummy nibh euismod tincidunt erat volutpat.<br><br>Ut wisi enim ad minim veniam, quis nostrud exerci tation ullamcorper suscipit lobortis nisl ut aliquip ex ea commodo consequat. Ut wisi enim ad minim veniam, quis nostrud exerci tation ullamcorper.</div>
  <div class="foot">torvusa.com</div><div class="pg">3</div>
</section>

<!-- 5 part one -->
<section class="slide c2 r2">
  <div class="part" role="img" aria-label="Background photo: refinery towers tinted slate"></div>
  <div class="partflag"></div>
  <div class="partbox"></div>
  <div class="partnum">01</div>
  <div class="parttitle">Part one</div>
  <div class="partsub">Lorem ipsum dolor sit amet, consectetuer adipiscing elit, sed diam nonummy nibh<br><br>laoreet dolore magna aliquam erat volutpat. Ut wisi enim ad minim veniam, quis nostrud exerci tation</div>
</section>

<!-- 6 values -->
<section class="slide c3 r2">
  <div class="title big" style="left:30px;top:20px">Lorem Ipsum<br>Dolor Sit<br>Ametkeeper.</div>
  <div class="logo">TORV</div>
  <div class="abs tx" style="left:0;top:140px;width:190px;height:98px;background:var(--slate);color:#fff;padding:14px 18px 0 30px">Lorem ipsum dolor sit amet, consectetuer adipiscing elit, sed diam nonummy nibh euismod tincidunt erat volutpat.<br><br>Ut wisi enim ad minim veniam, quis nostrud exerci tation ullamcorper suscipit lobortis nisl ut aliquip ex ea commodo consequat.</div>
  <div class="icon red" style="left:217px;top:62px"><svg width="18" height="14" viewBox="0 0 18 14" fill="#fff"><circle cx="5" cy="4" r="2.5"/><circle cx="13" cy="4" r="2.5"/><circle cx="9" cy="6" r="2.5"/><rect x="1" y="8" width="16" height="5" rx="2"/></svg></div>
  <div class="abs" style="left:258px;top:62px;width:210px"><div class="h6">We Before Me</div><div class="tx">Ipsum dolor sit amet, cons ectetuer adipiscing elit, sed diam nonummy nibh euismod tincidunt ut laoreet</div></div>
  <div class="icon red" style="left:217px;top:126px"><svg width="14" height="18" viewBox="0 0 14 18" fill="#fff"><circle cx="4" cy="3" r="2.2"/><circle cx="10" cy="3" r="2.2"/><rect x="1.5" y="6" width="5" height="11" rx="1"/><rect x="7.5" y="6" width="5" height="11" rx="1"/></svg></div>
  <div class="abs" style="left:258px;top:126px;width:210px"><div class="h6">We Are Good People</div><div class="tx">Ipsum dolor sit amet, cons ectetuer adipiscing elit, sed diam nonummy nibh euismod tincidunt ut laoreet dolore magna aliquam erat volutpat.</div></div>
  <div class="icon red" style="left:217px;top:197px"><svg width="18" height="16" viewBox="0 0 18 16" fill="#fff"><path d="M9 3c1-2 4-2 4 0.5S9 8 9 8 5 5 5 3.5 8 1 9 3z"/><path d="M1 11h4l3 2h6l3-3v5H1z"/></svg></div>
  <div class="abs" style="left:258px;top:197px;width:210px"><div class="h6">We Work with Heart</div><div class="tx">Ipsum dolor sit amet, cons ectetuer adipiscing elit, sed diam nonummy nibh euismod tincidunt</div></div>
  <div class="foot">torvusa.com</div><div class="pg">5</div>
</section>

<!-- 7 market chart -->
<section class="slide c1 r3">
  <div class="title big" style="left:22px;top:20px">Market<br>Opportunities.</div>
  <div class="logo">TORV</div>
  <div class="abs tx" style="left:22px;top:86px;width:140px;font-size:6px">Lorem ipsum dolor sit amet, consectetuer adipiscing elit, sed diam nonummy nibh euismod tincidunt ut laoreet dolore magna aliquam erat volutpat. Ut wisi enim ad minim veniam, quis nostrud exerci tation ullamcorper suscipit lobortis nisl ut aliquip ex ea commodo consequat. Duis autem vel eum iriure dolor in hendrerit.<br><br>Lorem ipsum dolor sit amet, consectetuer adipiscing elit, sed diam nonummy nibh.</div>
  <svg class="abs" style="left:200px;top:42px" width="290" height="150" viewBox="0 0 290 150" font-family="Montserrat, sans-serif">
    <text x="145" y="12" font-size="7" font-weight="600" text-anchor="middle" fill="#3a4150">Volume</text>
    <g stroke="#d6d8dc" stroke-width=".6">
      <line x1="30" y1="27" x2="285" y2="27"/><line x1="30" y1="40" x2="285" y2="40"/><line x1="30" y1="53" x2="285" y2="53"/><line x1="30" y1="66" x2="285" y2="66"/><line x1="30" y1="79" x2="285" y2="79"/><line x1="30" y1="92" x2="285" y2="92"/><line x1="30" y1="105" x2="285" y2="105"/><line x1="30" y1="118" x2="285" y2="118"/><line x1="30" y1="131" x2="285" y2="131" stroke="#999"/>
    </g>
    <g font-size="6" fill="#3a4150" text-anchor="end">
      <text x="22" y="29">160</text><text x="22" y="42">140</text><text x="22" y="55">120</text><text x="22" y="68">100</text><text x="22" y="81">80</text><text x="22" y="94">60</text><text x="22" y="107">40</text><text x="22" y="120">20</text><text x="22" y="133">0</text>
    </g>
    <rect x="46" y="86" width="20" height="45" fill="#4b5669"/>
    <rect x="105" y="53" width="20" height="78" fill="#b5281f"/>
    <rect x="163" y="33" width="20" height="98" fill="#4b5669"/>
    <rect x="221" y="43" width="20" height="88" fill="#b5281f"/>
    <g font-size="6" fill="#3a4150" text-anchor="middle"><text x="56" y="146">JAN</text><text x="115" y="146">FEB</text><text x="173" y="146">MAR</text><text x="231" y="146">APR</text></g>
  </svg>
  <div class="abs" style="left:200px;top:208px;width:120px"><div class="h6"><span class="dot"></span>Lorem ipsum</div><div class="tx" style="padding-left:8px">Lorem ipsum dolor sit amet, consectetuer adipiscing elit, sed diam nonummy nibh euismod tincidunt</div></div>
  <div class="abs" style="left:330px;top:208px;width:120px"><div class="h6"><span class="dot"></span>Lorem ipsum</div><div class="tx" style="padding-left:8px">Lorem ipsum dolor sit amet, consectetuer adipiscing elit, sed diam nonummy nibh euismod tincidunt</div></div>
  <div class="foot">torvusa.com</div><div class="pg">6</div>
</section>

<!-- 8 icon grid -->
<section class="slide c2 r3">
  <div class="title" style="left:17px;top:10px">Text Added Here</div>
  <div class="logo">TORV</div>
  <div class="icon red" style="left:88px;top:54px;width:32px;height:32px"><svg width="16" height="14" viewBox="0 0 16 14" fill="none" stroke="#fff" stroke-width="1.2"><circle cx="4" cy="4" r="2"/><circle cx="12" cy="4" r="2"/><circle cx="8" cy="5" r="2"/><path d="M1 12c0-3 6-3 6 0M9 12c0-3 6-3 6 0"/></svg></div>
  <div class="icon slate" style="left:214px;top:54px;width:32px;height:32px"><svg width="16" height="16" viewBox="0 0 16 16" fill="none" stroke="#fff" stroke-width="1.2"><circle cx="6" cy="6" r="4"/><circle cx="12" cy="11" r="3"/></svg></div>
  <div class="icon red" style="left:340px;top:54px;width:32px;height:32px"><svg width="16" height="16" viewBox="0 0 16 16" fill="#fff"><rect x="2" y="10" width="3" height="5"/><rect x="7" y="7" width="3" height="8"/><rect x="12" y="3" width="3" height="12"/></svg></div>
  <div class="icon slate" style="left:88px;top:143px;width:32px;height:32px"><svg width="16" height="16" viewBox="0 0 16 16" fill="none" stroke="#fff" stroke-width="1.2"><path d="M2 2v12h12M4 4l4 6 3-2 3 4"/></svg></div>
  <div class="icon red" style="left:214px;top:143px;width:32px;height:32px"><svg width="14" height="16" viewBox="0 0 14 16" fill="none" stroke="#fff" stroke-width="1.2"><path d="M5 2h4l-1 3c4 2 5 9 0 9H6C1 14 2 7 6 5z"/></svg></div>
  <div class="icon slate" style="left:340px;top:143px;width:32px;height:32px"><svg width="16" height="16" viewBox="0 0 16 16" fill="none" stroke="#fff" stroke-width="1.2"><circle cx="8" cy="8" r="5"/><path d="M8 5v3l2 2"/></svg></div>
  <div class="abs" style="left:44px;top:93px;width:120px;text-align:center"><div class="h6">Lorem Ipsum</div><div class="tx">Lorem ipsum dolor sit amet, consectetuer adipiscing elit, sed diam nonummy nibh euismod tincidunt ut laoreet</div></div>
  <div class="abs" style="left:170px;top:93px;width:120px;text-align:center"><div class="h6 red">Lorem Ipsum</div><div class="tx">Lorem ipsum dolor sit amet, consectetuer adipiscing elit, sed diam nonummy nibh euismod tincidunt ut laoreet</div></div>
  <div class="abs" style="left:296px;top:93px;width:120px;text-align:center"><div class="h6">Lorem Ipsum</div><div class="tx">Lorem ipsum dolor sit amet, consectetuer adipiscing elit, sed diam nonummy nibh euismod tincidunt ut laoreet</div></div>
  <div class="abs" style="left:44px;top:182px;width:120px;text-align:center"><div class="h6 red">Lorem Ipsum</div><div class="tx">Lorem ipsum dolor sit amet, consectetuer adipiscing elit, sed diam nonummy nibh euismod tincidunt ut laoreet</div></div>
  <div class="abs" style="left:170px;top:182px;width:120px;text-align:center"><div class="h6">Lorem Ipsum</div><div class="tx">Lorem ipsum dolor sit amet, consectetuer adipiscing elit, sed diam nonummy nibh euismod tincidunt ut laoreet</div></div>
  <div class="abs" style="left:296px;top:182px;width:120px;text-align:center"><div class="h6 red">Lorem Ipsum</div><div class="tx">Lorem ipsum dolor sit amet, consectetuer adipiscing elit, sed diam nonummy nibh euismod tincidunt ut laoreet</div></div>
  <div class="foot">torvusa.com</div><div class="pg">7</div>
</section>

<!-- 9 charts -->
<section class="slide c3 r3">
  <div class="title" style="left:17px;top:12px">Text Added Here</div>
  <div class="logo">TORV</div>
  <div class="abs tx" style="left:17px;top:46px;width:175px">Lorem ipsum dolor sit amet, consectetuer adipiscing elit, sed diam nonummy nibh euismod tincidunt ut laoreet dolore magna aliquam erat volutpat. Ut wisi enim ad minim veniam, quis nostrud exerci tation ullamcorper suscipit lobortis nisl ut aliquip ex ea commodo consequat. Duis</div>
  <svg class="abs" style="left:10px;top:110px" width="180" height="120" viewBox="0 0 180 120" font-family="Montserrat, sans-serif">
    <g font-size="7" fill="#3a4150" text-anchor="end"><text x="22" y="23">50%</text><text x="22" y="40">40%</text><text x="22" y="57">30%</text><text x="22" y="74">20%</text><text x="22" y="91">10%</text></g>
    <line x1="40" y1="10" x2="40" y2="100" stroke="#3a4150" stroke-width="1.2"/>
    <line x1="40" y1="100" x2="170" y2="100" stroke="#3a4150" stroke-width="1.2"/>
    <rect x="55" y="16" width="10" height="84" fill="#b5281f"/>
    <rect x="82" y="50" width="10" height="50" fill="#4b5669"/>
    <rect x="109" y="82" width="10" height="18" fill="#b5281f"/>
    <rect x="136" y="94" width="10" height="6" fill="#4b5669"/>
    <g font-size="7" fill="#3a4150" text-anchor="middle"><text x="60" y="115">1980</text><text x="87" y="115">1990</text><text x="114" y="115">2000</text><text x="141" y="115">2010</text></g>
  </svg>
  <svg class="abs" style="left:250px;top:55px" width="160" height="160" viewBox="0 0 160 160" font-family="Montserrat, sans-serif" fill="none">
    <circle cx="80" cy="80" r="74" stroke="#e6e7ea" stroke-width="3"/>
    <path d="M80 6 A74 74 0 1 1 12 51" stroke="#b5281f" stroke-width="3"/>
    <path d="M80 16 A64 64 0 1 1 16 80" stroke="#4b5669" stroke-width="3"/>
    <path d="M80 26 A54 54 0 0 1 118 118" stroke="#b5281f" stroke-width="3"/>
    <path d="M80 36 A44 44 0 0 1 118 100" stroke="#4b5669" stroke-width="3"/>
    <text x="80" y="84" font-size="11" fill="#4b5669" text-anchor="middle" font-weight="500">Add Text</text>
    <g font-size="6" font-weight="600"><text x="11" y="46" fill="#b5281f">68%</text><text x="24" y="118" fill="#4b5669">45%</text><text x="68" y="135" fill="#b5281f">35%</text><text x="111" y="116" fill="#4b5669">15%</text></g>
  </svg>
  <div class="abs" style="left:220px;top:215px;width:110px"><div class="h6" style="font-size:7px"><span class="dot"></span>Lorem Ipsum</div><div class="tx" style="padding-left:8px;font-size:4.5px">Lorem ipsum dolor sit amet, consectetuer adipiscing elit, sed diam nonummy nibh</div></div>
  <div class="abs" style="left:340px;top:215px;width:110px"><div class="h6" style="font-size:7px"><span class="dot"></span>Lorem Ipsum</div><div class="tx" style="padding-left:8px;font-size:4.5px">Lorem ipsum dolor sit amet, consectetuer adipiscing elit, sed diam nonummy nibh</div></div>
  <div class="foot">torvusa.com</div><div class="pg">8</div>
</section>

<!-- 10 two photos -->
<section class="slide c1 r4">
  <div class="logo">TORV</div>
  <div class="ph smoke" role="img" aria-label="Photo: chimneys of a power plant" style="left:15px;top:20px;width:80px;height:225px"></div>
  <div class="abs" style="left:160px;top:28px;width:330px;text-align:center;font-family:'Roboto Condensed',sans-serif;font-weight:500;font-size:19px;color:var(--slate)">Text Added Here<div style="width:32px;height:3px;background:var(--red);margin:6px auto 0"></div></div>
  <div class="abs tx" style="left:180px;top:66px;width:290px;text-align:center">Lorem ipsum dolor sit amet, consectetuer adipiscing elit, sed diam nonummy nibh euismod tincidunt erat volutpat. Ut wisi enim ad minim veniam, quis nostrud exerci tation ullamcorper suscipit<br><br>lobortis nisl ut aliquip ex ea commodo consequat. Ut wisi enim ad minim veniam, quis nostrud exerci tation ullamcorper suscipit do consequat. Ut wisi enim ad minim veniam, quis nostrud exerci tation ullamcorper suscipit lobortis nisl ut aliquip ex ea commodo consequat.</div>
  <div class="ph sunset" role="img" aria-label="Photo: industrial plant with smoke at sunrise" style="left:104px;top:142px;width:300px;height:102px"></div>
  <div class="foot">torvusa.com</div><div class="pg">9</div>
</section>

<!-- 11 two columns -->
<section class="slide c2 r4">
  <div class="title" style="left:17px;top:10px">Text Added Here</div>
  <div class="logo">TORV</div>
  <div class="abs" style="left:36px;top:55px;width:205px"><div class="h6 red" style="font-size:9px">1. Text Added Here</div><div class="tx j" style="margin-top:3px">Lorem ipsum dolor sit amet, cons ectetuer adipiscing elit, sed diam nonummy nibh euismod tincidunt ut laoreet dolore magna aliquam erat volutpat. Ut wisi enim ad minim veniam, quis nostrud exerci tation ullamcorper suscipit lobortis nisl ut aliquip ex ea commodo consequat.<br><br>Lorem ipsum dolor sit amet, consectetuer adipiscing elit, sed diam nonummy nibh euismod tincidunt ut laoreet dolore magna aliquam erat volutpat. Ut wisi enim ad minim veniam, quis nostrud exerci tation ullamcorper suscipit lobortis nisl ut aliquip ex ea commodo consequat.</div></div>
  <div class="abs" style="left:256px;top:55px;width:205px"><div class="h6 red" style="font-size:9px">2. Text Added Here</div><div class="tx j" style="margin-top:3px">Lorem ipsum dolor sit amet, cons ectetuer adipiscing elit, sed diam nonummy nibh euismod tincidunt ut laoreet dolore magna aliquam erat volutpat. Ut wisi enim ad minim veniam, quis nostrud exerci tation ullamcorper suscipit lobortis nisl ut aliquip ex ea commodo consequat.<br><br>Lorem ipsum dolor sit amet, consectetuer adipiscing elit, sed diam nonummy nibh euismod tincidunt ut laoreet dolore magna aliquam erat volutpat. Ut wisi enim ad minim veniam, quis nostrud exerci tation ullamcorper suscipit lobortis nisl ut aliquip ex ea commodo consequat.</div></div>
  <div class="abs" style="left:48px;top:165px"><span class="num red" style="width:18px;height:18px;font-size:9px">1.</span></div>
  <div class="abs" style="left:75px;top:165px;width:140px"><div class="h6">Lorem ipsum</div><div class="tx">Lorem ipsum dolor sit amet, consectetuer adipiscing elit, sed diam nonummy nibh</div></div>
  <div class="abs" style="left:48px;top:210px"><span class="num" style="width:18px;height:18px;font-size:9px">2.</span></div>
  <div class="abs" style="left:75px;top:210px;width:140px"><div class="h6">Lorem ipsum</div><div class="tx">Lorem ipsum dolor sit amet, consectetuer adipiscing elit, sed diam nonummy nibh</div></div>
  <div class="abs" style="left:272px;top:165px"><span class="num" style="width:18px;height:18px;font-size:9px">1.</span></div>
  <div class="abs" style="left:299px;top:165px;width:140px"><div class="h6">Lorem ipsum</div><div class="tx">Lorem ipsum dolor sit amet, consectetuer adipiscing elit, sed diam nonummy nibh</div></div>
  <div class="abs" style="left:272px;top:210px"><span class="num red" style="width:18px;height:18px;font-size:9px">2.</span></div>
  <div class="abs" style="left:299px;top:210px;width:140px"><div class="h6">Lorem ipsum</div><div class="tx">Lorem ipsum dolor sit amet, consectetuer adipiscing elit, sed diam nonummy nibh</div></div>
  <div class="foot">torvusa.com</div><div class="pg">10</div>
</section>

<!-- 12 numbered points -->
<section class="slide c3 r4">
  <div class="title" style="left:38px;top:20px">Text Added Here</div>
  <div class="logo">TORV</div>
  <div class="ph smoke" role="img" aria-label="Photo: cooling stacks in desert landscape" style="left:28px;top:55px;width:157px;height:185px"></div>
  <div class="abs" style="left:208px;top:70px"><span class="num red" style="width:28px;height:28px;border-radius:50%;font-size:13px">1</span></div>
  <div class="abs tx j" style="left:245px;top:73px;width:235px">Lorem ipsum dolor sit amet, consectetuer adipiscing elit, sed diam nonummy nibh euismod tincidunt ut laoreet dolore magna aliquam erat volutpat. Ut wisi enim ad minim veniam, quis nostrud exerci tation ullam-</div>
  <div class="abs" style="left:208px;top:133px"><span class="num red" style="width:28px;height:28px;border-radius:50%;font-size:13px">2</span></div>
  <div class="abs tx" style="left:245px;top:132px;width:235px">ullamcorper suscipit lobortis nisl ut aliquip ex ea commodo consequat. Duis autem vel eum iriure dolor in hendrerit in vulputate velit esse<br><br>molestie consequat, vel illum dolore eu feugiat nulla facilisis at vero eros</div>
  <div class="abs" style="left:208px;top:196px"><span class="num red" style="width:28px;height:28px;border-radius:50%;font-size:13px">3</span></div>
  <div class="abs tx j" style="left:245px;top:199px;width:235px">Lorem ipsum dolor sit amet, consectetuer adipiscing elit, sed diam nonummy nibh euismod tincidunt ut laoreet dolore magna aliquam erat volutpat. Ut wisi enim ad minim veniam, quis nostrud exerci tation ullam-</div>
  <div class="foot">torvusa.com</div><div class="pg">11</div>
</section>

<!-- 13 part two -->
<section class="slide c1 r5">
  <div class="part" role="img" aria-label="Background photo: refinery towers tinted slate"></div>
  <div class="partflag"></div>
  <div class="partbox"></div>
  <div class="partnum">02</div>
  <div class="parttitle">Part Two</div>
  <div class="partsub">Lorem ipsum dolor sit amet, consectetuer adipiscing elit, sed diam nonummy nibh<br><br>laoreet dolore magna aliquam erat volutpat. Ut wisi enim ad minim veniam, quis nostrud exerci tation</div>
</section>

<!-- 14 eight items -->
<section class="slide c2 r5">
  <div class="title" style="left:17px;top:10px">Text Added Here</div>
  <div class="logo">TORV</div>
  <div class="abs" style="left:40px;top:62px;width:200px">
    <div style="display:flex;gap:6px;margin-bottom:15px"><span class="num" style="min-width:24px;height:20px;font-size:10px">01.</span><div><div class="h6 red" style="font-size:7px">Aliquam Erat Volutpat</div><div class="tx">Lorem ipsum dolor sit amet, consectetuer adipiscing elit, sed diam nonummy nibh euismod</div></div></div>
    <div style="display:flex;gap:6px;margin-bottom:15px"><span class="num" style="min-width:24px;height:20px;font-size:10px">02.</span><div><div class="h6 red" style="font-size:7px">Consectetuer Adipiscing Elit</div><div class="tx">Lorem ipsum dolor sit amet, consectetuer adipiscing elit, sed diam nonummy nibh euismod tincidunt</div></div></div>
    <div style="display:flex;gap:6px;margin-bottom:15px"><span class="num" style="min-width:24px;height:20px;font-size:10px">03.</span><div><div class="h6 red" style="font-size:7px">Duis Autem Vel Eum</div><div class="tx">Lorem ipsum dolor sit amet, consectetuer adipiscing elit, sed diam nonummy nibh euismod tincidunt.</div></div></div>
    <div style="display:flex;gap:6px"><span class="num" style="min-width:24px;height:20px;font-size:10px">04.</span><div><div class="h6 red" style="font-size:7px">Aliquam Erat Volutpat</div><div class="tx">Lorem ipsum dolor sit amet, consectetuer adipiscing elit, sed diam nonummy nibh euismod tincidunt.</div></div></div>
  </div>
  <div class="abs" style="left:260px;top:62px;width:200px">
    <div style="display:flex;gap:6px;margin-bottom:15px"><span class="num" style="min-width:24px;height:20px;font-size:10px">05.</span><div><div class="h6 red" style="font-size:7px">Aliquam Erat Volutpat</div><div class="tx">Lorem ipsum dolor sit amet, consectetuer adipiscing elit, sed diam nonummy nibh euismod</div></div></div>
    <div style="display:flex;gap:6px;margin-bottom:15px"><span class="num" style="min-width:24px;height:20px;font-size:10px">06.</span><div><div class="h6 red" style="font-size:7px">Consectetuer Adipiscing Elit</div><div class="tx">Lorem ipsum dolor sit amet, consectetuer adipiscing elit, sed diam nonummy nibh euismod tincidunt</div></div></div>
    <div style="display:flex;gap:6px;margin-bottom:15px"><span class="num" style="min-width:24px;height:20px;font-size:10px">07.</span><div><div class="h6 red" style="font-size:7px">Duis Autem Vel Eum</div><div class="tx">Lorem ipsum dolor sit amet, consectetuer adipiscing elit, sed diam nonummy nibh euismod tincidunt.</div></div></div>
    <div style="display:flex;gap:6px"><span class="num" style="min-width:24px;height:20px;font-size:10px">08.</span><div><div class="h6 red" style="font-size:7px">Aliquam Erat Volutpat</div><div class="tx">Lorem ipsum dolor sit amet, consectetuer adipiscing elit, sed diam nonummy nibh euismod tincidunt.</div></div></div>
  </div>
  <div class="foot">torvusa.com</div><div class="pg">13</div>
</section>

<!-- 15 two photo columns -->
<section class="slide c3 r5">
  <div class="title big" style="left:25px;top:20px">Lorem Ipsum<br>Dolor Sit<br>Ametkeeper.</div>
  <div class="logo">TORV</div>
  <div class="abs tx" style="left:25px;top:110px;width:128px">Lorem ipsum dolor sit amet, consectetuer adipiscing elit, sed diam nonummy nibh euismod tincidunt ut laoreet dolore magna aliquam erat volutpat.<br><br>Ut wisi enim ad minim veniam, quis nostrud exerci tation ullamcorper suscipit lobortis nisl ut aliquip ex ea commodo consequat. Duis autem vel eum iriure dolor in hendrerit in vulputate velit esse molestie consequat,<br><br>vel illum dolore eu feugiat nulla facilisis at vero eros et accumsan et iusto odio dignissim qui blandit praesent luptatum zzril delenit augue duis dolore te feugait</div>
  <div class="ph field" role="img" aria-label="Photo: pumpjack at sunset" style="left:185px;top:55px;width:125px;height:78px"></div>
  <div class="ph plant" role="img" aria-label="Photo: refinery at dusk" style="left:335px;top:55px;width:125px;height:78px"></div>
  <div class="abs" style="left:185px;top:143px;width:125px"><div class="h6 red" style="font-size:10px">Dolor Sit</div><div class="tx">Lorem ipsum dolor sit amet, consectetuer adipiscing elit, sed diam nonummy nibh euismod tincidunt ut laoreet dolore magna<br><br>aliquam erat volutpat. Ut wisi enim ad minim veniam, quis nostrud exerci tation ullamcorper suscipit lobortis nisl ut aliquip</div></div>
  <div class="abs" style="left:335px;top:143px;width:125px"><div class="h6 red" style="font-size:10px">Laoreet Dolore</div><div class="tx">Lorem ipsum dolor sit amet, consectetuer adipiscing elit, sed diam nonummy nibh euismod tincidunt ut<br><br>laoreet dolore magna aliquam erat volutpat. Ut wisi enim ad minim veniam, quis nostrud exerci tation ullamcorper suscipit lobortis nisl ut aliquip ex ea</div></div>
  <div class="foot">torvusa.com</div><div class="pg">14</div>
</section>

<!-- 16 timemap -->
<section class="slide c1 r6">
  <div class="title" style="left:17px;top:10px">Our Timemap</div>
  <div class="logo">TORV</div>
  <svg class="abs" style="left:20px;top:60px" width="410" height="120" viewBox="0 0 410 120" font-family="Montserrat, sans-serif">
    <g font-size="7" font-weight="600" fill="#3a4150"><text x="22" y="18">2019</text><text x="22" y="54">2020</text><text x="22" y="90">2021</text></g>
    <circle cx="10" cy="15" r="3.5" fill="#b5281f"/><circle cx="10" cy="51" r="3.5" fill="#b5281f"/><circle cx="10" cy="87" r="3.5" fill="#b5281f"/>
    <g font-size="6" fill="#fff" text-anchor="middle">
      <rect x="72" y="2" width="45" height="26" fill="#b5281f"/><text x="94" y="17">20%</text>
      <rect x="117" y="2" width="68" height="26" fill="#4b5669"/><text x="151" y="17">40%</text>
      <rect x="185" y="2" width="45" height="26" fill="#b5281f"/><text x="207" y="17">10%</text>
      <rect x="230" y="2" width="168" height="26" fill="#4b5669"/><text x="314" y="17">90%</text>
      <rect x="72" y="38" width="108" height="26" fill="#4b5669"/><text x="126" y="53">50%</text>
      <rect x="180" y="38" width="72" height="26" fill="#b5281f"/><text x="216" y="53">30%</text>
      <rect x="252" y="38" width="83" height="26" fill="#4b5669"/><text x="293" y="53">20%</text>
      <rect x="335" y="38" width="63" height="26" fill="#b5281f"/><text x="366" y="53">20%</text>
      <rect x="72" y="74" width="60" height="26" fill="#4b5669"/><text x="102" y="89">30%</text>
      <rect x="132" y="74" width="87" height="26" fill="#b5281f"/><text x="175" y="89">60%</text>
      <rect x="219" y="74" width="48" height="26" fill="#4b5669"/><text x="243" y="89">10%</text>
      <rect x="267" y="74" width="131" height="26" fill="#b5281f"/><text x="332" y="89">70%</text>
    </g>
    <line x1="72" y1="108" x2="398" y2="108" stroke="#3a4150" stroke-width=".8"/>
    <g fill="#fff" stroke="#3a4150" stroke-width=".8"><circle cx="72" cy="108" r="2"/><circle cx="104" cy="108" r="2"/><circle cx="137" cy="108" r="2"/><circle cx="170" cy="108" r="2"/><circle cx="202" cy="108" r="2"/><circle cx="235" cy="108" r="2"/><circle cx="268" cy="108" r="2"/><circle cx="300" cy="108" r="2"/><circle cx="333" cy="108" r="2"/><circle cx="365" cy="108" r="2"/><circle cx="398" cy="108" r="2"/></g>
    <g font-size="5.5" fill="#3a4150" text-anchor="middle"><text x="72" y="119">0%</text><text x="104" y="119">10%</text><text x="137" y="119">20%</text><text x="170" y="119">30%</text><text x="202" y="119">40%</text><text x="235" y="119">50%</text><text x="268" y="119">60%</text><text x="300" y="119">70%</text><text x="333" y="119">80%</text><text x="365" y="119">90%</text><text x="398" y="119">100%</text></g>
  </svg>
  <div class="abs" style="left:85px;top:196px;width:70px"><div class="h6 red">Lorem Ipsum</div><div class="tx" style="font-size:4.5px">Lorem ipsum dolor sit amet, consectetuer adipiscing elit, sed diam nonummy nibh</div></div>
  <div class="abs" style="left:168px;top:196px;width:70px"><div class="h6 red">Lorem Ipsum</div><div class="tx" style="font-size:4.5px">Lorem ipsum dolor sit amet, consectetuer adipiscing elit, sed diam nonummy nibh</div></div>
  <div class="abs" style="left:251px;top:196px;width:70px"><div class="h6 red">Lorem Ipsum</div><div class="tx" style="font-size:4.5px">Lorem ipsum dolor sit amet, consectetuer adipiscing elit, sed diam nonummy nibh</div></div>
  <div class="abs" style="left:334px;top:196px;width:70px"><div class="h6 red">Lorem Ipsum</div><div class="tx" style="font-size:4.5px">Lorem ipsum dolor sit amet, consectetuer adipiscing elit, sed diam nonummy nibh</div></div>
  <div class="foot">torvusa.com</div><div class="pg">15</div>
</section>

<!-- 17 wide photo steps -->
<section class="slide c2 r6">
  <div class="title" style="left:17px;top:10px">Text Added Here</div>
  <div class="logo">TORV</div>
  <div class="ph smoke" role="img" aria-label="Photo: aerial view of cooling towers releasing steam" style="left:46px;top:60px;width:404px;height:118px"></div>
  <div class="abs" style="left:36px;top:170px"><span class="num red" style="width:26px;height:22px;font-size:11px">01</span></div>
  <div class="abs tx" style="left:68px;top:185px;width:90px">Lorem ipsum Dolor sit amet Consectetur adipiscing<br><br>sed do eiusmod Tempor incididunt ut labore et dolore</div>
  <div class="abs" style="left:176px;top:170px"><span class="num red" style="width:26px;height:22px;font-size:11px">02</span></div>
  <div class="abs tx" style="left:208px;top:185px;width:90px">Lorem ipsum Dolor sit amet Consectetur adipiscing<br><br>sed do eiusmod Tempor incididunt ut labore et dolore</div>
  <div class="abs" style="left:316px;top:170px"><span class="num red" style="width:26px;height:22px;font-size:11px">03</span></div>
  <div class="abs tx" style="left:348px;top:185px;width:90px">Lorem ipsum Dolor sit amet Consectetur adipiscing<br><br>sed do eiusmod Tempor incididunt ut labore et dolore</div>
  <div class="foot">torvusa.com</div><div class="pg">16</div>
</section>

<!-- 18 process steps -->
<section class="slide c3 r6">
  <div class="title" style="left:17px;top:10px">Text Added Here</div>
  <div class="logo">TORV</div>
  <svg class="abs" style="left:30px;top:80px" width="440" height="90" viewBox="0 0 440 90" font-family="Montserrat, sans-serif">
    <line x1="5" y1="48" x2="425" y2="48" stroke="#b5281f" stroke-width="5"/>
    <line x1="330" y1="48" x2="425" y2="48" stroke="#4b5669" stroke-width="5"/>
    <path d="M423 42 L433 48 L423 54 Z" fill="#4b5669"/>
    <g fill="none" stroke-width="6">
      <path d="M63 46 A22 22 0 1 1 107 46" stroke="#b5281f"/>
      <path d="M143 46 A22 22 0 1 1 187 46" stroke="#4b5669"/>
      <path d="M223 46 A22 22 0 1 1 267 46" stroke="#b5281f"/>
      <path d="M303 46 A22 22 0 1 1 347 46" stroke="#4b5669"/>
    </g>
    <g fill="none" stroke="#3a4150" stroke-width="1.2">
      <circle cx="85" cy="25" r="8"/><path d="M85 20v5l3 2"/>
      <circle cx="165" cy="25" r="8" fill="#3a4150"/>
      <ellipse cx="245" cy="20" rx="7" ry="2.5"/><path d="M238 20v9c0 3 14 3 14 0v-9"/>
      <circle cx="323" cy="23" r="6"/><path d="M328 28l4 4"/>
    </g>
    <g font-size="5" fill="#fff" text-anchor="middle" font-weight="600"><text x="85" y="50">Step 01</text><text x="165" y="50">Step 02</text><text x="245" y="50">Step 03</text><text x="340" y="50">Step 04</text></g>
    <g stroke="#3a4150" stroke-width=".8"><line x1="85" y1="53" x2="85" y2="66"/><line x1="165" y1="53" x2="165" y2="66"/><line x1="245" y1="53" x2="245" y2="66"/><line x1="325" y1="53" x2="325" y2="66"/></g>
  </svg>
  <div class="abs" style="left:85px;top:160px;width:60px;text-align:center"><div class="h6">Lorem Ipsum</div><div class="tx" style="font-size:4.5px">Lorem ipsum dolor sit amet, consectetuer adipiscing elit, sed diam nonummy nibh euismod tincidunt ut laoreet dolore</div></div>
  <div class="abs" style="left:165px;top:160px;width:60px;text-align:center"><div class="h6">Lorem Ipsum</div><div class="tx" style="font-size:4.5px">Lorem ipsum dolor sit amet, consectetuer adipiscing elit, sed diam nonummy nibh euismod tincidunt ut laoreet dolore</div></div>
  <div class="abs" style="left:245px;top:160px;width:60px;text-align:center"><div class="h6">Lorem Ipsum</div><div class="tx" style="font-size:4.5px">Lorem ipsum dolor sit amet, consectetuer adipiscing elit, sed diam nonummy nibh euismod tincidunt ut laoreet dolore</div></div>
  <div class="abs" style="left:325px;top:160px;width:60px;text-align:center"><div class="h6">Lorem Ipsum</div><div class="tx" style="font-size:4.5px">Lorem ipsum dolor sit amet, consectetuer adipiscing elit, sed diam nonummy nibh euismod tincidunt ut laoreet dolore</div></div>
  <div class="foot">torvusa.com</div><div class="pg">17</div>
</section>

<!-- 19 bullets -->
<section class="slide c1 r7">
  <div class="title" style="left:17px;top:10px">Text Added Here</div>
  <div class="logo">TORV</div>
  <div class="abs" style="left:35px;top:55px;width:400px">
    <div style="margin-bottom:10px"><div class="h6" style="font-size:7px"><span style="color:var(--red)">▪</span> Aliquam Erat Volutpat</div><div class="tx">Lorem ipsum dolor sit amet, consectetuer adipiscing elit, sed diam nonummy nibh euismod tincidunt ut laoreet dolore magna aliquam erat volutpat. Ut wisi enim ad minim veniam, quis nostrud exerci tation ullamcorper suscipit lobortis nisl ut aliquip ex ea commodo consequat. Duis autem vel eum iriure dolor in hendrerit in vulputate velit esse molestie consequat, vel illum dolore eu</div></div>
    <div style="margin-bottom:10px"><div class="h6" style="font-size:7px"><span style="color:var(--red)">▪</span> Consectetuer Adipiscing Elit</div><div class="tx">Lorem ipsum dolor sit amet, consectetuer adipiscing elit, sed diam nonummy nibh euismod tincidunt ut laoreet dolore magna aliquam erat volutpat. Ut wisi enim ad minim veniam, quis nostrud exerci tation ullamcorper suscipit lobortis nisl ut aliquip ex ea commodo consequat. Duis autem vel eum iriure dolor in hendrerit in vulputate velit esse molestie consequat, vel illum dolore eu</div></div>
    <div style="margin-bottom:10px"><div class="h6" style="font-size:7px"><span style="color:var(--red)">▪</span> Duis Autem Vel Eum</div><div class="tx">Lorem ipsum dolor sit amet, consectetuer adipiscing elit, sed diam nonummy nibh euismod tincidunt ut laoreet dolore magna aliquam erat volutpat. Ut wisi enim ad minim veniam, quis nostrud exerci tation ullamcorper suscipit lobortis nisl ut aliquip ex ea commodo consequat. Duis autem vel eum iriure dolor in hendrerit in vulputate velit esse molestie consequat, vel illum dolore eu</div></div>
    <div><div class="h6" style="font-size:7px"><span style="color:var(--red)">▪</span> Aliquam Erat Volutpat</div><div class="tx">Lorem ipsum dolor sit amet, consectetuer adipiscing elit, sed diam nonummy nibh euismod tincidunt ut laoreet dolore magna aliquam erat volutpat. Ut wisi enim ad minim veniam, quis nostrud exerci tation ullamcorper suscipit lobortis nisl ut aliquip ex ea commodo consequat. Duis autem vel eum iriure dolor in hendrerit in vulputate velit esse molestie consequat, vel illum dolore eu</div></div>
  </div>
  <div class="foot">torvusa.com</div><div class="pg">18</div>
</section>

<!-- 20 team -->
<section class="slide c2 r7">
  <div class="title" style="left:17px;top:10px">Our Team</div>
  <div class="logo">TORV</div>
  <div class="abs tx j" style="left:30px;top:42px;width:440px">Lorem ipsum dolor sit amet, consectetuer adipiscing elit, sed diam nonummy nibh euismod tincidunt ut laoreet dolore magna aliquam erat volutpat. Ut wisi enim ad minim veniam, quis nostrud exerci tation ullamcorper suscipit lobortis nisl ut aliquip ex ea commodo consequat. Duis autem vel eum iriure dolor in hendrerit in vulputate velit esse molestie consequat, vel illum dolore eu feugiat nulla facilisis at vero eros et accumsan et iusto odio dignissim qui blandit praesent luptatum zzril delenit augue duis dolore te feugait nulla facilisi.<br><br>Lorem ipsum dolor sit amet, cons ectetuer adipiscing elit, sed diam nonummy nibh euismod tincidunt ut laoreet dolore magna aliquam erat volutpat. Ut wisi enim ad minim veniam, quis nostrud exerci tation ullamcorper suscipit lobortis nisl ut aliquip ex ea.</div>
  <div class="abs" style="left:0;top:136px;width:500px;height:88px;background:var(--slate)"></div>
  <div class="ph" role="img" aria-label="Team member portrait" style="left:48px;top:120px;width:32px;height:32px;border-radius:50%;border:2px solid var(--red);background:#c9ccd3"></div>
  <div class="ph" role="img" aria-label="Team member portrait" style="left:158px;top:120px;width:32px;height:32px;border-radius:50%;border:2px solid var(--red);background:#c9ccd3"></div>
  <div class="ph" role="img" aria-label="Team member portrait" style="left:268px;top:120px;width:32px;height:32px;border-radius:50%;border:2px solid var(--red);background:#c9ccd3"></div>
  <div class="ph" role="img" aria-label="Team member portrait" style="left:378px;top:120px;width:32px;height:32px;border-radius:50%;border:2px solid var(--red);background:#c9ccd3"></div>
  <div class="abs" style="left:24px;top:160px;width:80px;text-align:center;color:#fff"><div style="font-size:7px;font-weight:700">ARLEN BRASK</div><div class="tx" style="color:#fff;font-size:4px">Ipsum dolor sit amet, cons ectetuer adipiscing elit, sed diam nonummy nibh euismod tincidunt ut laoreet dolore magna aliquam erat volutpat. Ut wisi enim ad minim veniam, quis nostrud</div></div>
  <div class="abs" style="left:134px;top:160px;width:80px;text-align:center;color:#fff"><div style="font-size:7px;font-weight:700">NOA VIRELAND</div><div class="tx" style="color:#fff;font-size:4px">Ipsum dolor sit amet, cons ectetuer adipiscing elit, sed diam nonummy nibh euismod tincidunt ut laoreet dolore magna aliquam erat volutpat. Ut wisi enim ad minim veniam, quis nostrud</div></div>
  <div class="abs" style="left:244px;top:160px;width:80px;text-align:center;color:#fff"><div style="font-size:7px;font-weight:700">ARLEN BRASK</div><div class="tx" style="color:#fff;font-size:4px">Ipsum dolor sit amet, cons ectetuer adipiscing elit, sed diam nonummy nibh euismod tincidunt ut laoreet dolore magna aliquam erat volutpat. Ut wisi enim ad minim veniam, quis nostrud</div></div>
  <div class="abs" style="left:354px;top:160px;width:80px;text-align:center;color:#fff"><div style="font-size:7px;font-weight:700">NOA VIRELAND</div><div class="tx" style="color:#fff;font-size:4px">Ipsum dolor sit amet, cons ectetuer adipiscing elit, sed diam nonummy nibh euismod tincidunt ut laoreet dolore magna aliquam erat volutpat. Ut wisi enim ad minim veniam, quis nostrud</div></div>
  <div class="foot">torvusa.com</div><div class="pg">19</div>
</section>

<!-- 21 thank you -->
<section class="slide c3 r7">
  <div class="abs" style="left:0;top:22px;width:500px;text-align:center;font-weight:800;font-size:32px;color:var(--ink);letter-spacing:1px">TORV</div>
  <div class="abs" style="left:70px;top:120px;width:110px;text-align:right;font-family:'Roboto Condensed',sans-serif;font-weight:700;font-size:36px;line-height:1.05;color:var(--slate)">Thank<br>You</div>
  <div class="ph plant" role="img" aria-label="Photo: refinery units under evening sky" style="left:195px;top:102px;width:150px;height:155px"></div>
  <div class="abs" style="left:360px;top:102px;width:23px;height:155px;background:var(--red)"></div>
  <div class="abs" style="left:360px;top:102px;width:23px;height:155px;display:flex;align-items:center;justify-content:center"><span style="transform:rotate(-90deg);white-space:nowrap;color:#fff;font-size:11px;font-weight:600;letter-spacing:2px">torvusa.com</span></div>
  <div class="abs" style="left:12px;top:255px;width:13px;height:13px;background:var(--red)"></div>
</section>

</body>
</html>
```